Fur Haven Animal Hospital Postcard Design

I need a postcard for grand opening. The front of the card should have our business name and logo, below the logo I want to have a coupon for " Free office visit or $ 20 off of packages " for the first time clients.

I want to have the packages prices and details on the back of the postcard, the details of the packages are attached.

```html
<!DOCTYPE html>
<html lang="en">
<head>
<meta charset="utf-8">
<title>Fur Haven Animal Hospital – Grand Opening Postcard</title>
<link rel="stylesheet" href="https://fonts.googleapis.com/css2?family=Arimo:wght@400;700&family=Open+Sans:wght@400;600&display=swap">
<style>
  :root{
    --blue:#1496d6;
    --blue-deep:#0b6fae;
    --blue-light:#2bb0ea;
    --orange:#f07f10;
    --green:#6cbf2a;
    --peach:#fdeedf;
    --ink:#1b4f7a;
    --text:#2a3a4a;
    --white:#ffffff;
    --bg:#d9dbdd;
  }
  *{box-sizing:border-box;margin:0;padding:0}
  html,body{width:1200px;height:1200px;overflow:hidden;background:var(--bg)}
  body{position:relative;font-family:"Arimo",Arial,sans-serif}

  .card{position:absolute;top:80px;width:500px;height:1040px;overflow:hidden;box-shadow:0 6px 18px rgba(0,0,0,.25)}

  /* Front */
  .front{left:55px;background:linear-gradient(180deg,var(--blue-light) 0%,var(--blue) 45%,var(--blue-deep) 100%)}
  .front__logo{position:absolute;top:40px;width:100%;text-align:center;color:var(--white);font-weight:700;font-size:118px;letter-spacing:2px;line-height:1}
  .front__photo-ring{position:absolute;left:40px;top:270px;width:420px;height:420px;border-radius:50%;border:3px solid var(--white);
    background:radial-gradient(circle at 50% 40%,#8fbf5a 0%,#5f9a3a 55%,#3d6e2a 100%)}
  .front__photo-subject{position:absolute;left:160px;top:175px;width:190px;height:510px;border-radius:90px 90px 40px 40px;
    background:linear-gradient(180deg,#d99a4a 0%,#c07a2c 60%,#a8661f 100%)}
  .coupon{position:absolute;left:338px;top:620px;width:150px;height:150px;border-radius:50%;background:var(--white);border:3px solid var(--green);
    text-align:center;padding-top:20px;color:var(--text);font-weight:700}
  .coupon__free{color:var(--orange);font-size:34px;line-height:1}
  .coupon__small{font-size:13px;line-height:1.15}
  .coupon__or{color:#e0262a;font-size:14px;margin:6px 0 2px}
  .coupon__off{color:var(--orange);font-size:26px;line-height:1}
  .front__name{position:absolute;left:0;top:840px;width:100%;text-align:center;color:var(--white);font-weight:700;line-height:1}
  .front__name span{display:block}
  .front__name .l1{font-size:62px;letter-spacing:1px}
  .front__name .l2{font-size:42px;margin-top:6px}
  .front__wave{position:absolute;left:0;bottom:0;width:500px;height:90px}
  .front__web{position:absolute;bottom:30px;width:100%;text-align:center;color:var(--white);font-size:13px;letter-spacing:2.5px}

  /* Back */
  .back{left:645px;background:var(--white)}
  .back__header{position:absolute;top:0;left:0;width:500px;height:200px}
  .back__title{position:absolute;top:38px;width:100%;text-align:center;font-weight:700;line-height:1}
  .back__title .l1{display:block;color:var(--white);font-size:60px;letter-spacing:1px}
  .back__title .l2{display:block;color:var(--orange);font-size:42px;margin-top:4px}

  .packages{position:absolute;top:232px;left:18px;width:464px;display:grid;grid-template-columns:1fr 1fr;gap:26px 12px}
  .package{background:var(--peach);padding:10px 10px 10px 10px;height:128px}
  .package__title{color:var(--ink);font-size:11px;font-weight:700;text-transform:uppercase}
  .package__label{color:var(--ink);font-size:11px;font-weight:700;margin:8px 0 7px}
  .package__lists{display:flex;justify-content:space-between;font-family:"Open Sans",Arial,sans-serif;font-size:9px;color:var(--text)}
  .package__lists ul{list-style:none}
  .package__lists li{line-height:1.75;padding-left:10px;position:relative}
  .package__lists li::before{content:"";position:absolute;left:0;top:6px;width:4px;height:4px;border-radius:50%;background:var(--ink)}

  .back__footer{position:absolute;left:0;bottom:0;width:500px;height:250px}
  .back__pets{position:absolute;left:60px;top:0;width:210px;height:110px;border-radius:50px 50px 10px 10px;background:linear-gradient(180deg,#c8a27a,#7d6a5a)}
  .back__people{position:absolute;left:270px;top:10px;width:220px;height:200px;border-radius:90px 90px 20px 20px;background:linear-gradient(180deg,#f1e3c8 0%,#b9cfe6 70%,#8fb6dc 100%)}
  .back__wave{position:absolute;left:0;bottom:0;width:500px;height:160px}
  .contact{position:absolute;left:40px;bottom:28px;color:var(--white)}
  .contact__head{font-weight:700;font-size:15px;margin-bottom:10px}
  .contact__row{display:flex;align-items:center;gap:8px;font-size:17px;margin-bottom:6px}
  .contact__row--web{font-size:11px}
  .contact__row svg{flex:none}
</style>
</head>
<body>

<section class="card front" aria-label="Postcard front">
  <div class="front__logo">LOGO</div>
  <div class="front__photo-ring" role="img" aria-label="Garden with flowers and lawn"></div>
  <div class="front__photo-subject" role="img" aria-label="Golden retriever sitting in the garden"></div>
  <div class="coupon">
    <div class="coupon__free">FREE</div>
    <div class="coupon__small">Office Visit</div>
    <div class="coupon__or">OR</div>
    <div class="coupon__off">$ 20 OFF</div>
    <div class="coupon__small">of Packages</div>
  </div>
  <h1 class="front__name"><span class="l1">FUR HAVEN</span><span class="l2">ANIMAL HOSPITAL</span></h1>
  <svg class="front__wave" viewBox="0 0 500 90" preserveAspectRatio="none" aria-hidden="true">
    <path d="M0 70 Q250 -10 500 30 L500 90 L0 90 Z" fill="var(--blue-light)"/>
  </svg>
  <div class="front__web">www.furhavenanimalhospital.com</div>
</section>

<section class="card back" aria-label="Postcard back">
  <svg class="back__header" viewBox="0 0 500 200" preserveAspectRatio="none" aria-hidden="true">
    <path d="M0 0 H500 V110 Q260 240 0 160 Z" fill="var(--blue-deep)"/>
    <path d="M0 160 Q260 240 500 110" fill="none" stroke="var(--green)" stroke-width="3"/>
  </svg>
  <h2 class="back__title"><span class="l1">FUR HAVEN</span><span class="l2">ANIMAL HOSPITAL</span></h2>

  <div class="packages">
    <article class="package">
      <h3 class="package__title">Annual Dog Package $99</h3>
      <p class="package__label">INCLUDES</p>
      <div class="package__lists">
        <ul><li>Complete Physical Exam</li><li>DHLPP Vaccine</li><li>Bordetella Vaccine</li><li>Rabies Vaccine</li></ul>
        <ul><li>Fecal Exam</li><li>Heartworm Test</li><li>Deworming</li></ul>
      </div>
    </article>
    <article class="package">
      <h3 class="package__title">Puppy Package 1 [7-10 Weeks] $49</h3>
      <p class="package__label">INCLUDES</p>
      <div class="package__lists">
        <ul><li>Complete Physical Exam</li><li>DHLPP Vaccine</li><li>Bordetella Vaccine</li></ul>
        <ul><li>Fecal Exam</li><li>Deworming</li></ul>
      </div>
    </article>
    <article class="package">
      <h3 class="package__title">Puppy Package 2 [10-13 Weeks] $49</h3>
      <p class="package__label">INCLUDES</p>
      <div class="package__lists">
        <ul><li>Complete Physical Exam</li><li>DHLPP Vaccine</li><li>Bordetella Vaccine</li></ul>
        <ul><li>Fecal Exam</li><li>Deworming</li></ul>
      </div>
    </article>
    <article class="package">
      <h3 class="package__title">Puppy Package 3 [13-16 Weeks] $49</h3>
      <p class="package__label">INCLUDES</p>
      <div class="package__lists">
        <ul><li>Complete Physical Exam</li><li>DHLPP Vaccine</li><li>Rabies Vaccine</li></ul>
        <ul><li>Fecal Exam</li><li>Deworming</li></ul>
      </div>
    </article>
    <article class="package">
      <h3 class="package__title">Annual Cat Package $69</h3>
      <p class="package__label">INCLUDES</p>
      <div class="package__lists">
        <ul><li>Complete Physical Exam</li><li>FVRCP Vaccine</li><li>Rabies Vaccine</li></ul>
        <ul><li>Fecal Exam</li><li>Deworming</li></ul>
      </div>
    </article>
    <article class="package">
      <h3 class="package__title">Kitten Package 1 [7-10 Weeks] $49</h3>
      <p class="package__label">INCLUDES</p>
      <div class="package__lists">
        <ul><li>Complete Physical Exam</li><li>FVRCP Vaccine</li></ul>
        <ul><li>Fecal Exam</li><li>Deworming</li></ul>
      </div>
    </article>
    <article class="package">
      <h3 class="package__title">Kitten Package 2 [10-13 Weeks] $49</h3>
      <p class="package__label">INCLUDES</p>
      <div class="package__lists">
        <ul><li>Complete Physical Exam</li><li>FVRCP Vaccine</li></ul>
        <ul><li>Fecal Exam</li><li>Deworming</li></ul>
      </div>
    </article>
    <article class="package">
      <h3 class="package__title">Kitten Package 3 [13-16 Weeks] $49</h3>
      <p class="package__label">INCLUDES</p>
      <div class="package__lists">
        <ul><li>Complete Physical Exam</li><li>FVRCP Vaccine</li></ul>
        <ul><li>Fecal Exam</li><li>Deworming</li></ul>
      </div>
    </article>
  </div>

  <div class="back__footer">
    <div class="back__pets" role="img" aria-label="Dog and cat peeking over the edge"></div>
    <svg class="back__wave" viewBox="0 0 500 160" preserveAspectRatio="none" aria-hidden="true">
      <path d="M0 40 Q250 -10 500 30 L500 160 L0 160 Z" fill="var(--blue)"/>
      <path d="M0 40 Q250 -10 500 30" fill="none" stroke="var(--green)" stroke-width="3"/>
    </svg>
    <div class="back__people" role="img" aria-label="Woman sitting with a golden retriever"></div>
    <div class="contact">
      <p class="contact__head">CONTACT US :</p>
      <p class="contact__row">
        <svg width="16" height="16" viewBox="0 0 24 24" aria-hidden="true"><path d="M6.6 10.8a15 15 0 0 0 6.6 6.6l2.2-2.2a1 1 0 0 1 1-.25 11.4 11.4 0 0 0 3.6.57 1 1 0 0 1 1 1V20a1 1 0 0 1-1 1A17 17 0 0 1 3 4a1 1 0 0 1 1-1h3.5a1 1 0 0 1 1 1c0 1.25.2 2.45.57 3.57a1 1 0 0 1-.25 1z" fill="none" stroke="#fff" stroke-width="1.6"/></svg>
        (555) 014-2290
      </p>
      <p class="contact__row contact__row--web">
        <svg width="14" height="14" viewBox="0 0 24 24" aria-hidden="true"><circle cx="12" cy="12" r="10" fill="none" stroke="#fff" stroke-width="1.8"/><path d="M2 12h20M12 2c3 3 3 17 0 20M12 2c-3 3-3 17 0 20" fill="none" stroke="#fff" stroke-width="1.5"/></svg>
        www.furhavenanimalhospital.com
      </p>
    </div>
  </div>
</section>

</body>
</html>
```